Business card design for Allied Healthcare provider

We would like a design for front and back of business cards. The design must resonate with all levels of customers from patients, to other health providers and medical. Must also resonate with corporate customers

Target Market(s)

patients, medical practitioners, other health providers and corporate.

Industry/Entity Type

healthcare

Contact Information for Business Card

name, logo, phone and fax numbers, email, website

Requirements
Must have
• not allowing me to change this, but the card must be double sided!! Please take note
Nice to have
• a fresh yet bold design to catch attention.

```html
<!DOCTYPE html>
<html lang="en">
<head>
<meta charset="utf-8">
<title>vitalwell business card</title>
<link rel="stylesheet" href="https://fonts.googleapis.com/css2?family=Nunito:wght@700;800;900&family=Arimo:wght@400&display=swap">
<style>
  :root {
    --navy: #0e2763;
    --gold: #f5bd1f;
    --white: #ffffff;
    --ink: #1c1c22;
    --stage: #2b2b2e;
  }
  * { margin: 0; padding: 0; box-sizing: border-box; }
  html, body { width: 1200px; height: 900px; overflow: hidden; }
  body {
    background: var(--stage);
    font-family: "Nunito", sans-serif;
    position: relative;
  }
  .card {
    position: absolute;
    left: 250px;
    width: 700px;
    height: 400px;
    overflow: hidden;
  }
  .card-front { top: 40px; background: var(--navy); }
  .card-back { top: 460px; background: var(--white); }

  .front-brand {
    position: absolute;
    left: 0; right: 0; top: 148px;
    text-align: center;
  }
  .brand-name {
    display: inline-flex;
    align-items: center;
    gap: 14px;
    font-weight: 800;
    font-size: 62px;
    line-height: 1;
    letter-spacing: 1px;
  }
  .brand-dot {
    width: 26px; height: 26px;
    border-radius: 50%;
    background: var(--gold);
  }
  .front-brand .brand-name { color: var(--white); }
  .tagline {
    margin-top: 8px;
    color: var(--gold);
    font-weight: 700;
    font-size: 21px;
    letter-spacing: 1.5px;
  }

  .back-brand { position: absolute; left: 40px; top: 40px; }
  .back-brand .brand-name { color: var(--navy); font-size: 54px; }

  .holder {
    position: absolute;
    right: 58px; top: 172px;
    text-align: right;
  }
  .holder-name {
    color: var(--navy);
    font-weight: 900;
    font-size: 36px;
    letter-spacing: 1px;
    line-height: 1;
  }
  .holder-role {
    color: var(--gold);
    font-family: "Arimo", sans-serif;
    font-size: 18px;
    line-height: 1.2;
    margin-top: 4px;
  }
  .holder-rule {
    position: absolute;
    right: 150px; top: 226px;
    width: 220px; height: 1.5px;
    background: var(--gold);
  }
  .side-tab {
    position: absolute;
    right: 0; top: 160px;
    width: 16px; height: 74px;
    background: var(--navy);
    border-radius: 8px 0 0 8px;
  }
  .divider {
    position: absolute;
    left: 40px; right: 40px; top: 270px;
    height: 1.5px;
    background: var(--gold);
  }
  .contacts {
    position: absolute;
    left: 46px; top: 284px;
    list-style: none;
    font-family: "Arimo", sans-serif;
    font-size: 19px;
    color: var(--ink);
  }
  .contacts li {
    display: flex;
    align-items: center;
    gap: 22px;
    height: 24px;
  }
  .contacts svg { width: 18px; height: 18px; flex: none; }
  .icon-fill { fill: var(--navy); }
  .icon-line { fill: none; stroke: var(--navy); }
</style>
</head>
<body>
  <section class="card card-front" aria-label="Card front">
    <div class="front-brand">
      <div class="brand-name"><span class="brand-dot"></span>vitalwell</div>
      <p class="tagline">care · comfort · wellbeing</p>
    </div>
  </section>

  <section class="card card-back" aria-label="Card back">
    <div class="back-brand">
      <div class="brand-name"><span class="brand-dot"></span>vitalwell</div>
    </div>

    <div class="side-tab"></div>
    <div class="holder">
      <p class="holder-name">Marco Delani</p>
      <p class="holder-role">Manager</p>
    </div>
    <div class="holder-rule"></div>

    <div class="divider"></div>

    <ul class="contacts">
      <li>
        <svg viewBox="0 0 24 24" aria-hidden="true"><path class="icon-fill" d="M6.6 10.8a15.1 15.1 0 0 0 6.6 6.6l2.2-2.2a1 1 0 0 1 1-.25 11.4 11.4 0 0 0 3.6.57 1 1 0 0 1 1 1V20a1 1 0 0 1-1 1A17 17 0 0 1 3 4a1 1 0 0 1 1-1h3.5a1 1 0 0 1 1 1c0 1.25.2 2.45.57 3.57a1 1 0 0 1-.25 1z"/></svg>
        <span>0123 456788</span>
      </li>
      <li>
        <svg viewBox="0 0 24 24" aria-hidden="true"><path class="icon-fill" d="M7 3h10v5H7zM4 9h16a2 2 0 0 1 2 2v6h-4v4H6v-4H2v-6a2 2 0 0 1 2-2zm4 6v4h8v-4z"/></svg>
        <span>0123 456789</span>
      </li>
      <li>
        <svg viewBox="0 0 24 24" aria-hidden="true"><path class="icon-fill" d="M2 5h20v14H2zm2 2v.5l8 5.5 8-5.5V7zm0 3v7h16v-7l-8 5.5z"/></svg>
        <span>info@yourwebsite.com</span>
      </li>
      <li>
        <svg viewBox="0 0 24 24" aria-hidden="true"><g class="icon-line" stroke-width="1.8"><circle cx="12" cy="12" r="9.5"/><ellipse cx="12" cy="12" rx="4" ry="9.5"/><path d="M2.5 12h19M4 7h16M4 17h16"/></g></svg>
        <span>www.yourwebsite.com</span>
      </li>
    </ul>
  </section>
</body>
</html>
```